Medical Herbalist needs labels for healing skin salves

I am bringing out a Calendula Salve and a Comfrey and Meadowsweet Salve, both have healing qualities and have have a history of Traditional use. I would like the label to look eye-cathching and colourful, orange based for Calendula and Green based for Comfrey. I particularly like Varembelle's image and their font. (skin care range - please look at this) I want to convey a sense of the Apothecary (most important) and slightly retro, old fashioned, quality about these salves.
I would like a design to fit on a label that goes around a 30ml or 60ml jar - I will be using both. I feel that the usp is that I am a Medical Herbalist producing hand made, containing natural ingredients - quality items made in Wales. (part of the UK) I have considered calling them Tidy Tins but not definite about this yet.
Measurements:
60ml jar - 31mm (height) x 150 to 160mm width - i.e. around the jar
30ml jar 18mm (height) x 105mm to 125mm width - i.e. around the jar

Reason: I would like to see some more designs before I make my decisions - I have not had enough that I am excited about so far I am afraid.

Target Market(s)

Adults, male and female but female bias. Wanting to solve problem i.e. dry chapped skin, cracked heals (Calendula). Sprains, aches and pains (Comfrey and Meadowsweet)

Industry/Entity Type

Medical

Font styles to use
Serif
Decorative

Colors
acd036
cadf82
e9f1ce
f79020
fece3e
faa54b

Requirements
Must have
• The kind of font and look I have suggested. Clearly Calendula Salve in large writing
and the same for the Comfrey and Meadowsweet Salve. It needs to have some impact
I need to have room to list ingredients.
Nice to have
• Possible images of the plants or part of the plants listed. I was not intending the photographs to be used - they were more to inspire hopefully.
Picture of pestle and mortar?
Should not have
• Anything too jokey or gimmicky.

```html
<!DOCTYPE html>
<html lang="en">
<head>
<meta charset="utf-8">
<title>Comfrey &amp; Meadowsweet Salve Label</title>
<link rel="stylesheet" href="https://fonts.googleapis.com/css2?family=Sorts+Mill+Goudy:ital@0;1&display=swap">
<style>
  :root {
    --lime: #acd036;
    --lime-soft: #cadf82;
    --lime-pale: #e9f1ce;
    --cream: #fbf8e6;
    --stripe: #f1ecd3;
    --tan: #d4cb9c;
    --tan-dark: #b9ad74;
    --tan-pale: #ebe6c6;
    --ink: #4f4a2a;
    --white: #ffffff;
  }
  * { margin: 0; padding: 0; box-sizing: border-box; }
  html, body { width: 1200px; height: 265px; overflow: hidden; background: var(--white); }
  .label {
    position: relative;
    width: 1200px;
    height: 265px;
    overflow: hidden;
    font-family: "Sorts Mill Goudy", Georgia, serif;
    color: var(--ink);
  }
  .label-frame { position: absolute; inset: 0; }
  .maker-panel {
    position: absolute;
    left: 38px; top: 42px; width: 206px; height: 190px;
    background: var(--tan-pale);
    text-align: center;
    padding-top: 8px;
  }
  .maker-name {
    font-variant: small-caps;
    font-size: 33px;
    line-height: 32px;
    letter-spacing: 0.5px;
  }
  .maker-title {
    font-variant: small-caps;
    font-size: 19px;
    letter-spacing: 1px;
    margin: 4px 10px 0;
    padding-top: 4px;
    border-top: 1px solid var(--tan-dark);
  }
  .maker-address {
    font-variant: small-caps;
    font-size: 16px;
    line-height: 22px;
    text-align: left;
    padding: 8px 0 0 12px;
  }
  .plant-art {
    position: absolute;
    border-radius: 50%;
  }
  .plant-art--meadowsweet {
    left: 255px; top: 48px; width: 215px; height: 185px;
    background: radial-gradient(ellipse at 35% 40%, #f2ead0 0%, #dfe9b4 45%, rgba(233,241,206,0) 72%);
  }
  .plant-art--comfrey {
    left: 725px; top: 35px; width: 225px; height: 200px;
    background: radial-gradient(ellipse at 50% 50%, #c6e07a 0%, #dceba9 45%, rgba(233,241,206,0) 72%);
  }
  .product-title {
    position: absolute;
    left: 465px; top: 80px; width: 265px;
    text-align: center;
    font-style: italic;
    font-weight: normal;
    font-size: 36px;
    line-height: 41px;
  }
  .claim-panel {
    position: absolute;
    left: 958px; top: 35px; width: 208px; height: 157px;
    background: var(--tan-pale);
    font-style: italic;
    font-size: 21px;
    line-height: 25px;
    text-align: center;
    padding-top: 17px;
  }
  .volume {
    position: absolute;
    left: 815px; top: 215px;
    font-size: 16px;
  }
  .batch-box {
    position: absolute;
    left: 995px; top: 200px; width: 171px; height: 28px;
    border: 1.5px solid var(--lime);
    background: var(--white);
    font-size: 6px;
    letter-spacing: 0.3px;
    padding: 3px 5px;
    color: var(--tan-dark);
  }
  .recycle-icon { position: absolute; left: 958px; top: 202px; }
</style>
</head>
<body>
<div class="label">
  <svg class="label-frame" width="1200" height="265" viewBox="0 0 1200 265" aria-hidden="true">
    <defs>
      <pattern id="paper-stripes" width="8" height="8" patternUnits="userSpaceOnUse">
        <rect width="8" height="8" fill="#fbf8e6"/>
        <rect y="6" width="8" height="1" fill="#f1ecd3"/>
      </pattern>
    </defs>
    <rect width="1200" height="265" fill="#d4cb9c"/>
    <rect x="0" y="8" width="1200" height="249" fill="#acd036"/>
    <rect x="7" y="14" width="1186" height="237" fill="none" stroke="#ffffff" stroke-width="1.5" stroke-dasharray="3 3"/>
    <rect x="18" y="22" width="1164" height="221" fill="url(#paper-stripes)"/>
    <rect x="555" y="0" width="86" height="265" fill="#d4cb9c"/>
    <ellipse cx="598" cy="140" rx="134" ry="110" fill="#d4cb9c"/>
    <ellipse cx="598" cy="142" rx="120" ry="98" fill="#fbf8e6"/>
    <ellipse cx="598" cy="142" rx="114" ry="92" fill="none" stroke="#d4cb9c" stroke-width="1.5"/>
    <circle class="seal-dot" cx="598" cy="48" r="19" fill="#b9ad74"/>
  </svg>

  <div class="maker-panel">
    <div class="maker-name">Morwenna<br>Pryce</div>
    <div class="maker-title">Medical Herbalist</div>
    <div class="maker-address">Nant, Cwmderyn,<br>Llanfedwy, Ceredigion,<br>Wales SA48 7QX.</div>
  </div>

  <div class="plant-art plant-art--meadowsweet" role="img" aria-label="Illustration of a flowering meadowsweet sprig"></div>
  <div class="plant-art plant-art--comfrey" role="img" aria-label="Illustration of a comfrey stem with leaves and flowers"></div>

  <h1 class="product-title">Comfrey &amp;<br>Meadowsweet<br>Salve</h1>

  <p class="claim-panel">Traditionally used<br>to relieve<br>muscular aches,<br>strains and sprains</p>

  <p class="volume">e 60ml. (2 fl. oz.)</p>

  <svg class="recycle-icon" width="22" height="24" viewBox="0 0 22 24" aria-hidden="true">
    <circle cx="11" cy="12" r="10" fill="none" stroke="#acd036" stroke-width="1.5"/>
    <rect x="6" y="8" width="10" height="9" rx="1.5" fill="none" stroke="#acd036" stroke-width="1.5"/>
    <line x1="8" y1="11" x2="14" y2="11" stroke="#acd036" stroke-width="1"/>
  </svg>
  <div class="batch-box">BATCH NO.</div>
</div>
</body>
</html>
```